Updated look for company collateral

We are a staffing company specializing in placing accounting, finance and IT professionals in their next career. We are going through a rebrand as well, i have included several other pieces so you can see our vision for the future. We are looking for a front and back one pager. We have four divisions Our company needs an updated look for our company collateral - there are four versions of the content (Enterprise, IT, Healthcare IT and Accounting & Finance) the design will be the same (different images for each flyer but same template) I am looking for a template that could be updated for each division. I am including the content for the IT version.

Our design aesthetic is clean, well organized, but with interesting design elements. We want to be perceived as on trend, leader in our industry. We have been in business for almost 20 years and know our industry well and successfully, our workforce is youthful, energetic and competitive so we still want to have an element of fun and creativity in our collateral.

Font styles to use
Sans Serif

Requirements
Must have
• similar color themes as attached examples

```html
<!DOCTYPE html>
<html lang="en">
<head>
<meta charset="utf-8">
<title>Vantor Staffing – One Pager</title>
<link href="https://fonts.googleapis.com/css2?family=Oswald:wght@500;700&family=Montserrat:wght@400;500;600;700;800&display=swap" rel="stylesheet">
<style>
:root{
  --orange:#f7941d;
  --charcoal:#3d3d3f;
  --ink:#333335;
  --text:#4a4a4c;
  --band-text:#dcdcdc;
  --tab:#ececec;
  --backdrop:#e6e6e6;
  --white:#ffffff;
}
*{box-sizing:border-box;margin:0;padding:0}
html,body{width:1200px;height:2357px;overflow:hidden}
body{background:var(--backdrop);font-family:"Montserrat",Arial,sans-serif;color:var(--text);position:relative}
.page{position:absolute;left:200px;width:800px;height:1130px;background:var(--white);overflow:hidden;box-shadow:0 4px 14px rgba(0,0,0,.18)}
.page--front{top:30px}
.page--back{top:1197px}
.abs{position:absolute}

/* front header */
.hero-title{left:43px;top:44px;font-family:"Oswald",Arial,sans-serif;font-weight:700;font-size:64px;line-height:70px;color:var(--ink);letter-spacing:.3px;white-space:nowrap}
.hero-title .accent{color:var(--orange)}
.hero-sub{left:43px;top:286px;font-family:"Oswald",Arial,sans-serif;font-weight:500;font-size:22px;line-height:27px;color:var(--ink)}
.hero-accent{left:462px;top:0;width:14px;height:380px;background:var(--orange)}
.hero-photo{left:488px;top:0;width:312px;height:380px}
.hero-corner{left:488px;top:0;width:312px;height:14px;background:var(--orange)}

/* dark band */
.intro-band{left:0;top:380px;width:800px;height:178px;background:var(--charcoal)}
.band-col{position:absolute;top:14px}
.band-col--left{left:43px;width:355px}
.band-col--right{left:423px;width:340px}
.band-heading{font-weight:700;font-size:20px;color:var(--orange);margin-bottom:4px}
.band-copy{font-size:10.6px;line-height:12.6px;color:var(--band-text);text-align:justify}

/* strategic model */
.section-heading{font-weight:700;font-size:18px;color:var(--orange);text-decoration:underline;text-underline-offset:3px}
.model-heading{left:43px;top:572px}
.model-copy{left:43px;top:604px;width:714px;font-size:10.4px;line-height:11.8px;color:var(--text);text-align:justify}
.model-copy p{margin-bottom:6px}

/* metrics */
.metric{position:absolute;width:330px;padding-left:33px}
.metric .tick{position:absolute;left:0;top:2px;width:20px;height:20px}
.metric-name{font-weight:700;font-size:18px;color:var(--orange);line-height:21px}
.metric-desc{font-size:18px;line-height:19px;color:var(--ink)}

/* footer */
.footer-tab{left:0;top:1030px;width:340px;height:100px}
.brand{position:absolute;left:0;top:1040px;width:310px;text-align:center}
.brand-dot{display:block;margin:0 auto 8px;width:38px;height:38px;border-radius:50%;background:var(--orange)}
.brand-name{font-weight:600;font-size:20px;letter-spacing:2.5px;color:var(--ink)}
.footer-bar{left:319px;top:1070px;width:481px;height:60px;background:var(--charcoal);display:flex;align-items:center;justify-content:flex-end;padding-right:40px;gap:10px;color:var(--white);font-size:12px;font-weight:700}
.footer-bar .sep{opacity:.8}
.footer-bar svg{width:14px;height:14px}
.social{display:flex;gap:7px}
.social span{width:18px;height:18px;border-radius:50%;background:var(--white)}

/* back */
.team-photo{left:0;top:0;width:800px;height:306px}
.cap-heading{left:44px;top:328px;font-weight:800;font-size:25px;line-height:28px;color:var(--ink)}
.cap-heading .accent{color:var(--orange)}
.cap-intro{left:44px;top:400px;width:714px;font-size:11px;line-height:12.5px}
.checks{position:absolute;font-weight:700;font-size:15px;color:var(--ink);padding-left:29px;line-height:18px}
.checks svg{position:absolute;left:0;top:0;width:19px;height:19px}
.sub-heading{font-weight:700;font-size:17px;color:var(--orange)}
.copy{font-size:11px;line-height:12.5px;color:var(--text)}
.copy p{margin-bottom:6px}
.block-heading{font-weight:700;font-size:19px;color:var(--orange);line-height:21px}
.block-copy{font-size:13.5px;line-height:15px;color:var(--ink)}
.office{position:absolute;font-size:16px;color:var(--ink);padding-left:20px}
.office svg{position:absolute;left:0;top:1px;width:14px;height:18px}
</style>
</head>
<body>

<svg width="0" height="0" style="position:absolute">
  <defs>
    <symbol id="icon-tick" viewBox="0 0 24 24">
      <path d="M20 11.2A8.5 8.5 0 1 1 14.5 3.8" fill="none" stroke="currentColor" stroke-width="2.2" stroke-linecap="round"/>
      <path d="M7.5 11.5l4 4L21 5.5" fill="none" stroke="currentColor" stroke-width="2.4" stroke-linecap="round" stroke-linejoin="round"/>
    </symbol>
    <symbol id="icon-pin" viewBox="0 0 14 18">
      <path d="M7 0a6 6 0 0 0-6 6c0 4.5 6 12 6 12s6-7.5 6-12a6 6 0 0 0-6-6zm0 8.3A2.3 2.3 0 1 1 7 3.7a2.3 2.3 0 0 1 0 4.6z" fill="currentColor"/>
    </symbol>
    <symbol id="icon-globe" viewBox="0 0 16 16">
      <circle cx="8" cy="8" r="6.5" fill="none" stroke="currentColor" stroke-width="1.6"/>
      <path d="M1.5 8h13M8 1.5c-3 3.5-3 9.5 0 13M8 1.5c3 3.5 3 9.5 0 13" fill="none" stroke="currentColor" stroke-width="1.3"/>
    </symbol>
    <symbol id="icon-phone" viewBox="0 0 16 16">
      <path d="M2 5c0-2 2-3 6-3s6 1 6 3v1h-3.5V4.8h-5V6H2z M4 7h8l2 6H2z" fill="currentColor"/>
    </symbol>
    <linearGradient id="hero-photo-tone" x1="0" y1="0" x2="1" y2="1">
      <stop offset="0" stop-color="#7fa8cf"/>
      <stop offset=".55" stop-color="#3d5f86"/>
      <stop offset="1" stop-color="#c9b8a8"/>
    </linearGradient>
    <linearGradient id="office-photo-tone" x1="0" y1="0" x2="1" y2="1">
      <stop offset="0" stop-color="#d9d4cc"/>
      <stop offset=".5" stop-color="#8c8a88"/>
      <stop offset="1" stop-color="#e4dfd6"/>
    </linearGradient>
  </defs>
</svg>

<!-- FRONT -->
<section class="page page--front">
  <h1 class="abs hero-title"><span class="accent">POWERING</span><br>PROGRESSION<br>WITH PEOPLE</h1>
  <p class="abs hero-sub">RECRUITMENT SOLUTIONS FOR AN<br>EVOLVING MARKETPLACE.</p>

  <div class="abs hero-accent"></div>
  <svg class="abs hero-photo" viewBox="0 0 312 380"><rect width="312" height="380" fill="url(#hero-photo-tone)" role="img" aria-label="Photo of two confident young professionals in business attire looking upward"/></svg>
  <div class="abs hero-corner"></div>

  <div class="abs intro-band">
    <div class="band-col band-col--left">
      <h2 class="band-heading">Vantor Staffing</h2>
      <p class="band-copy">For over 20 years we have cultivated relationships with some of the most talented IT professionals. We are their trusted partner assisting them as they achieve their career goals. Our team is focused on matching that talent with the positions you have available and ensuring they align with your organization's goals and culture. Finding the right talent takes time and you away from your work, let Vantor Staffing be your talent acquisition partner for your IT staffing needs.</p>
    </div>
    <div class="band-col band-col--right">
      <h2 class="band-heading">Client Services</h2>
      <p class="band-copy">Our IT recruiting team understands the challenges facing hiring managers and the need to find the right people quickly. Our dynamic processes scale to meet the needs of ever-changing business environments. When you need IT resources for project or permanent opportunities, Vantor Staffing is committed to providing innovative solutions that deliver consistent results.</p>
    </div>
  </div>

  <h2 class="abs section-heading model-heading">Strategic Staffing Model</h2>
  <div class="abs model-copy">
    <p>Vantor Staffing partners with clients nationwide to deliver the right resources to meet project and permanent staffing goals. Your dedicated recruiting team is committed to matching you with top talent to meet budget and staffing goals, while maintaining consistency and communication throughout the recruiting process.</p>
    <p>We take the time to get to know you, your organization and culture to ensure we recruit the right professionals for your team. Then we take the same amount of care to get to know candidates so you only interview individuals with the right skillsets and career goals.</p>
    <p>Transparency and communication are at our core and you can expect to have one point of contact, fast feedback and open dialogue with our team throughout the recruiting process. As part of our commitment to transparency and process improvement, we monitor and provide metrics to ensure we always provide the best service to our clients, including</p>
  </div>

  <div class="metric" style="left:47px;top:775px"><svg class="tick" style="color:var(--ink)"><use href="#icon-tick"/></svg><div class="metric-name">Candidate Accuracy Rate</div><div class="metric-desc">Percentage of presented<br>candidates who interview</div></div>
  <div class="metric" style="left:47px;top:857px"><svg class="tick" style="color:var(--ink)"><use href="#icon-tick"/></svg><div class="metric-name">Interview to Hire Rate</div><div class="metric-desc">Percentage of interviewees<br>who are hired</div></div>
  <div class="metric" style="left:47px;top:937px"><svg class="tick" style="color:var(--ink)"><use href="#icon-tick"/></svg><div class="metric-name">Placement Success Rate</div><div class="metric-desc">Customer satisfaction<br>for each placement</div></div>
  <div class="metric" style="left:397px;top:775px;width:380px"><svg class="tick" style="color:var(--ink)"><use href="#icon-tick"/></svg><div class="metric-name">Fulfillment Ratio</div><div class="metric-desc">Percentage of requests<br>fulfilled vs. the competition</div></div>
  <div class="metric" style="left:397px;top:857px;width:380px"><svg class="tick" style="color:var(--ink)"><use href="#icon-tick"/></svg><div class="metric-name">Time to Fill Ratio</div><div class="metric-desc">Time it takes from initial<br>request to candidate presentation</div></div>
  <div class="metric" style="left:397px;top:937px;width:380px"><svg class="tick" style="color:var(--ink)"><use href="#icon-tick"/></svg><div class="metric-name">Total Billing</div><div class="metric-desc">Total services billed<br>per quarter</div></div>

  <svg class="abs footer-tab" viewBox="0 0 340 100"><path d="M0 0H295L340 100H0Z" fill="var(--tab)"/></svg>
  <div class="brand"><span class="brand-dot"></span><span class="brand-name">VANTOR STAFFING</span></div>
  <div class="abs footer-bar">
    <svg style="color:var(--orange)"><use href="#icon-globe"/></svg><span>www.vantorstaffing.com</span><span class="sep">|</span>
    <svg style="color:var(--orange)"><use href="#icon-phone"/></svg><span>(615) 555-0142</span><span class="sep">|</span>
    <span class="social"><span></span><span></span><span></span></span>
  </div>
</section>

<!-- BACK -->
<section class="page page--back">
  <svg class="abs team-photo" viewBox="0 0 800 306"><rect width="800" height="306" fill="url(#office-photo-tone)" role="img" aria-label="Photo of a diverse team smiling around a meeting table in a bright office"/></svg>

  <h2 class="abs cap-heading"><span class="accent">Enterprise Managed</span><br>Service Capabilities</h2>
  <p class="abs cap-intro">Vantor Staffing works closely with enterprise clients who utilize VMS and MPS solutions and provide the following services as part of our commitment to our clients.</p>

  <div class="checks" style="left:44px;top:458px"><svg style="color:var(--orange)"><use href="#icon-tick"/></svg>Attract top talent</div>
  <div class="checks" style="left:44px;top:489px"><svg style="color:var(--orange)"><use href="#icon-tick"/></svg>Accountability</div>
  <div class="checks" style="left:44px;top:520px"><svg style="color:var(--orange)"><use href="#icon-tick"/></svg>Evaluation</div>
  <div class="checks" style="left:255px;top:458px"><svg style="color:var(--orange)"><use href="#icon-tick"/></svg>Customized reporting</div>
  <div class="checks" style="left:255px;top:489px"><svg style="color:var(--orange)"><use href="#icon-tick"/></svg>Consolidated billing</div>
  <div class="checks" style="left:496px;top:458px"><svg style="color:var(--orange)"><use href="#icon-tick"/></svg>Structured approval process</div>
  <div class="checks" style="left:496px;top:489px"><svg style="color:var(--orange)"><use href="#icon-tick"/></svg>Standardized terms</div>

  <h3 class="abs sub-heading" style="left:44px;top:564px">Who is Vantor Staffing?</h3>
  <div class="abs copy" style="left:44px;top:586px;width:714px">
    <p>Vantor Staffing specializes in Accounting &amp; Finance, IT and Healthcare IT staffing. We put the right people in the right jobs for their career goals and the business goals of our clients.</p>
    <p>Our objective is to create long term relationships that exceed our client's expectations. Our mission and values outline the commitments we make to each client and consultant.</p>
  </div>

  <h3 class="abs sub-heading" style="left:44px;top:654px">What makes Vantor Staffing different?</h3>
  <p class="abs copy" style="left:44px;top:676px;width:714px">There are many choices you can make for when looking for a staffing partner, and our goal is to be your staffing partner of choice.</p>

  <div class="abs" style="left:44px;top:728px;width:345px">
    <div class="block-heading">Team:</div>
    <div class="block-copy">Consists of passionate, experienced recruiters who place talent with our long-term partners.</div>
  </div>
  <div class="abs" style="left:44px;top:796px;width:345px">
    <div class="block-heading">Experience:</div>
    <div class="block-copy">With 20 years in the industry, we know staffing and what makes a good team member for our clients. We have strong networks of professionals that includes some of the best in their respective industries.</div>
  </div>
  <div class="abs" style="left:425px;top:728px;width:335px">
    <div class="block-heading">Strategic partnerships:</div>
    <div class="block-copy">we work with clients whose values align with ours to provide world class recruiting services.</div>
  </div>
  <div class="abs" style="left:425px;top:796px;width:335px">
    <div class="block-heading">Internal processes:</div>
    <div class="block-copy">Everything we do is driven by our internal processes to ensure the highest level of service and we review our metrics to ensure we work with the maximum efficiency.</div>
  </div>

  <h3 class="abs sub-heading" style="left:44px;top:928px">Office locations</h3>
  <div class="office" style="left:44px;top:962px"><svg style="color:var(--ink)"><use href="#icon-pin"/></svg>Headquarters in Nashville</div>
  <div class="office" style="left:44px;top:1000px"><svg style="color:var(--ink)"><use href="#icon-pin"/></svg>Boca Raton, FL</div>
  <div class="office" style="left:363px;top:962px"><svg style="color:var(--ink)"><use href="#icon-pin"/></svg>Atlanta, GA</div>
  <div class="office" style="left:363px;top:1000px"><svg style="color:var(--ink)"><use href="#icon-pin"/></svg>Denver, CO</div>
  <div class="office" style="left:603px;top:962px"><svg style="color:var(--ink)"><use href="#icon-pin"/></svg>Birmingham, AL</div>
  <div class="office" style="left:603px;top:1000px"><svg style="color:var(--ink)"><use href="#icon-pin"/></svg>Louisville, KY</div>

  <svg class="abs footer-tab" viewBox="0 0 340 100"><path d="M0 0H295L340 100H0Z" fill="var(--tab)"/></svg>
  <div class="brand"><span class="brand-dot"></span><span class="brand-name">VANTOR STAFFING</span></div>
  <div class="abs footer-bar">
    <svg style="color:var(--orange)"><use href="#icon-globe"/></svg><span>www.vantorstaffing.com</span><span class="sep">|</span>
    <svg style="color:var(--orange)"><use href="#icon-phone"/></svg><span>(615) 555-0142</span><span class="sep">|</span>
    <span class="social"><span></span><span></span><span></span></span>
  </div>
</section>

</body>
</html>
```